Flooring Company Wordpress Design Using Elementor

We need a website design using elementor for a flooring company. I have attached a word document with the entire content for the site. I have sample websites www.pellingtonrenovatesutah.com and www.stonepathtilesdenver.com

The site needs to look alot better than the samples. Modern and professional is what we are looking for. 100 times better than the sample websites.

I have images to be used in the site but the file is to large to attached here.

```html
<!DOCTYPE html>
<html lang="en">
<head>
<meta charset="utf-8">
<title>Keystone Flooring Florida</title>
<link href="https://fonts.googleapis.com/css2?family=Oswald:wght@400;500;600&family=Roboto:wght@400;500;700&family=Poppins:wght@400;600&family=Lobster&display=swap" rel="stylesheet">
<style>
:root{
  --yellow:#f5b21b;
  --yellow-dark:#e5a210;
  --dark:#333333;
  --darker:#2a2a2a;
  --grey-bg:#e9e9e9;
  --light-bg:#f4f4f4;
  --text:#555;
  --white:#fff;
}
*{box-sizing:border-box;margin:0;padding:0}
html,body{width:1200px;height:4570px;overflow:hidden}
body{position:relative;font-family:'Roboto',sans-serif;color:var(--text);background:var(--white)}
.abs{position:absolute}
.btn{position:absolute;display:flex;align-items:center;justify-content:center;font:500 10px 'Roboto',sans-serif;text-transform:uppercase;color:var(--white);background:var(--yellow)}
.btn-dark{background:var(--dark)}
.btn-outline{background:transparent;border:1px solid #555;color:var(--white)}

/* header */
.site-header{top:0;left:0;width:1200px;height:85px;background:var(--white)}
.brand{position:absolute;display:flex;align-items:center;gap:8px;font:600 22px 'Oswald',sans-serif;color:var(--darker);letter-spacing:.5px}
.brand-mark{width:14px;height:14px;background:var(--yellow)}
.hours{position:absolute;left:830px;top:22px;width:130px;text-align:right;font-size:9px;color:#777;line-height:20px}
.hours span{display:block;border-bottom:1px solid var(--yellow)}
.nav{top:85px;left:0;width:1200px;height:54px;border-top:1px solid #e4e4e4;border-bottom:1px solid #e4e4e4;background:var(--white)}
.nav ul{position:absolute;left:108px;top:0;height:52px;display:flex;list-style:none}
.nav li{display:flex;align-items:center;padding:0 11px;font:400 10.5px 'Oswald',sans-serif;text-transform:uppercase;color:var(--darker)}
.nav li.active{background:var(--yellow);color:var(--white)}
.social{position:absolute;top:13px;display:flex;gap:10px}
.social i{display:block;width:26px;height:26px;background:#555}

/* hero */
.hero{top:139px;left:0;width:1200px;height:577px;background:linear-gradient(100deg,#8d8a84 0%,#b3b0aa 45%,#77736d 100%)}
.hero-copy{position:absolute;right:152px;top:130px;width:560px;text-align:right;color:var(--white)}
.hero-copy .kicker{font:400 27px 'Oswald',sans-serif}
.hero-copy h1{font:600 66px/1.05 'Oswald',sans-serif;color:var(--yellow);text-transform:uppercase}
.hero-copy p{margin-top:10px;font-size:11.5px;line-height:21px}

/* features */
.features{top:716px;left:0;width:1200px;height:599px;background:var(--grey-bg)}
.feature{position:absolute;top:0;width:302px;text-align:center}
.feature .icon{position:absolute;top:55px;left:101px;width:100px;height:95px;border-radius:6px}
.feature h3{position:absolute;top:195px;width:100%;font:400 16px 'Oswald',sans-serif;text-transform:uppercase;color:var(--darker)}
.feature h3.accent{color:var(--yellow)}
.feature p{position:absolute;top:242px;width:100%;font-size:11.5px;line-height:21px;text-align:justify;color:#555}
.divider{position:absolute;top:130px;width:1px;height:345px;background:#cfcfcf}
.warranty{position:absolute;top:470px;width:1200px;text-align:center;font:400 40px 'Lobster',sans-serif;color:var(--yellow)}
.warranty b{color:var(--darker);font-weight:400}

/* partner */
.partner{top:1315px;left:0;width:1200px;height:489px;background:var(--dark)}
.partner h2{position:absolute;left:117px;top:84px;font:500 26px 'Oswald',sans-serif;color:var(--yellow);text-transform:uppercase}
.partner p{position:absolute;left:117px;top:142px;width:451px;font-size:11.5px;line-height:26.5px;text-align:justify;color:#ddd}
.photo{position:absolute}

/* services */
.services{top:1813px;left:0;width:1200px;height:1060px;background:var(--white)}
.section-title{position:absolute;width:1200px;text-align:center;font:500 27px 'Oswald',sans-serif;color:var(--darker);text-transform:uppercase}
.section-sub{position:absolute;width:1200px;text-align:center;font-size:11.5px;color:#777}
.card{position:absolute;width:302px;height:373px;background:var(--dark)}
.card .img{position:absolute;top:0;left:0;width:302px;height:147px}
.card h3{position:absolute;top:170px;width:100%;text-align:center;font:400 16px 'Oswald',sans-serif;text-transform:uppercase;color:var(--white)}
.card h3.accent{color:var(--yellow)}
.card p{position:absolute;top:213px;left:24px;width:254px;font-size:11px;line-height:21px;text-align:center;color:#ccc}
.card .btn{top:320px;height:30px;width:106px}
.card .b1{left:35px}.card .b2{left:152px}

/* reviews */
.reviews{top:2880px;left:0;width:1200px;height:595px;background:var(--white)}
.map{position:absolute;left:180px;top:70px;width:840px;height:330px;background:radial-gradient(ellipse at center,#f1f1f1 0%,#fafafa 60%,#fff 100%)}
.reviews h2{position:absolute;top:100px;width:1200px;text-align:center;font:400 41px/50px 'Poppins',sans-serif;color:var(--darker)}
.reviews h2 b{font-weight:600}
.review{position:absolute;top:284px;width:327px;height:231px;background:var(--white);box-shadow:0 4px 18px rgba(0,0,0,.09)}
.review .quote{position:absolute;left:26px;top:-14px;width:30px;height:30px;border-radius:50%;background:var(--yellow);color:var(--white);font:700 18px/34px 'Poppins',sans-serif;text-align:center}
.review .avatar{position:absolute;left:32px;top:-8px;width:86px;height:86px;border-radius:50%;background:linear-gradient(135deg,#9a8c80,#4f4a47)}
.review .stars{position:absolute;right:30px;top:38px;color:var(--yellow);font-size:16px;letter-spacing:3px}
.review p{position:absolute;left:30px;top:98px;width:270px;font:400 14px/25px 'Poppins',sans-serif;color:#444}
.review .name{position:absolute;left:30px;top:186px;font:600 16px 'Poppins',sans-serif;color:var(--darker)}
.review .name span{font:400 11px 'Poppins',sans-serif;color:#999}
.dots{position:absolute;top:558px;left:575px;display:flex;gap:6px}
.dots i{display:block;width:20px;height:6px;border-radius:3px;background:var(--yellow)}
.dots i+i{background:#555}

/* process */
.process{top:3475px;left:0;width:1200px;height:343px;background:linear-gradient(180deg,var(--yellow) 0%,#eba915 100%)}
.process .section-title{top:34px;color:var(--white)}
.process .section-sub{top:76px;color:#fff3d6}
.step{position:absolute;top:118px;width:240px;text-align:center}
.step .circle{margin:0 auto;width:80px;height:80px;border-radius:50%;background:var(--dark);border:3px solid #fff3d6;display:flex;align-items:center;justify-content:center}
.step .circle .fill{width:38px;height:38px;border-radius:50%;background:linear-gradient(135deg,#5a5a5a,#444)}
.step h4{margin-top:18px;font:500 15px 'Oswald',sans-serif;color:var(--darker)}
.step p{margin:10px auto 0;width:212px;font-size:11.5px;line-height:21px;color:var(--white);text-align:justify}

/* form */
.get-started{top:3818px;left:0;width:1200px;height:350px;background:var(--light-bg)}
.get-started h2{position:absolute;left:110px;top:126px;font:500 27px 'Oswald',sans-serif;color:var(--darker)}
.get-started .lead{position:absolute;left:110px;top:170px;width:300px;font-size:12px;line-height:24px;color:#666}
.field{position:absolute;width:212px;height:36px;border-bottom:1px solid #bbb;font-size:11.5px;color:#555}
.submit{position:absolute;left:442px;top:308px;width:251px;height:26px;background:var(--yellow);color:var(--white);font:500 11px 'Roboto',sans-serif;display:flex;align-items:center;justify-content:center}

/* footer */
.footer{top:4168px;left:0;width:1200px;height:347px;background:var(--white)}
.search{position:absolute;left:373px;top:68px;width:462px;height:34px;border:1px solid #ddd;box-shadow:0 2px 6px rgba(0,0,0,.06);font-size:11px;color:#999;padding:10px 12px}
.contact-list{position:absolute;left:108px;top:142px;list-style:none;font-size:11px;line-height:27px;color:#555}
.contact-list li::before{content:"+";color:var(--yellow);margin-right:10px;font-weight:700}
.col{position:absolute;top:142px}
.col h5{font:700 12px 'Roboto',sans-serif;color:var(--darker);text-transform:uppercase}
.col ul{list-style:none;margin-top:18px;border-left:1px solid #ccc;padding-left:10px}
.col li{font-size:11px;line-height:25px;color:#555;text-transform:uppercase}
.col li::before{content:"";display:inline-block;width:8px;height:1px;background:#ccc;vertical-align:middle;margin-right:8px}
.promise{position:absolute;left:858px;top:68px;width:253px;height:164px;background:var(--white);box-shadow:0 3px 14px rgba(0,0,0,.1);padding:22px 26px}
.promise h5{font:700 12px 'Roboto',sans-serif;color:var(--darker)}
.promise ul{list-style:none;margin-top:14px}
.promise li{font-size:10px;font-weight:500;line-height:26px;color:var(--darker)}
.promise li::before{content:"";display:inline-block;width:9px;height:9px;border-radius:50%;background:var(--yellow);margin-right:12px}
.pay{position:absolute;top:266px;display:flex;gap:14px;left:858px}
.pay i{display:block;width:44px;height:28px;background:#d9dde5;border-radius:2px}
.bottom-bar{top:4515px;left:0;width:1200px;height:55px;background:#f2f2f2;font-size:10px;color:#777}
</style>
</head>
<body>

<header class="site-header abs">
  <div class="brand" style="left:108px;top:27px"><span class="brand-mark"></span>KEYSTONE FLOORING FLORIDA</div>
  <div class="hours"><span>MON - FRI 8AM - 5PM</span>(02) 555 010 000</div>
  <div class="btn" style="left:985px;top:26px;width:107px;height:36px;font-family:'Oswald',sans-serif;font-size:11px;color:var(--darker)">Schedule Now</div>
</header>

<nav class="nav abs">
  <ul>
    <li class="active">Home</li><li>Tile Installation</li><li>Commercial Portfolio</li><li>Bathroom Tile Installation</li><li>Tile Backsplash Installation</li><li>Service Areas</li><li>Floor Removal</li>
  </ul>
  <div class="social" style="left:942px"><i></i><i></i><i></i><i></i></div>
</nav>

<section class="hero abs" role="img" aria-label="Photo of a bright living room with a mustard armchair on a grey tiled floor">
  <div class="hero-copy">
    <div class="kicker">Change your building flooring story with</div>
    <h1>Keystone Group</h1>
    <p>Are you tired of having your residential or commercial floors messed up by unprofessional services? Allow Keystone Group to change your floor installation and removal story today with our premium services, creativity, and personalized approach.</p>
  </div>
  <div class="btn btn-dark" style="left:790px;top:335px;width:77px;height:32px">Explore</div>
  <div class="btn" style="left:888px;top:335px;width:160px;height:32px">Get Your Free Estimate</div>
</section>

<section class="features abs">
  <div class="feature" style="left:107px">
    <div class="icon" style="background:linear-gradient(180deg,#d8d8d8 0%,#c9c2b0 100%)" role="img" aria-label="Illustration of a worker laying floor tiles"></div>
    <h3 class="accent">Minimal Stress On Your Plate</h3>
    <p>Floor installation or removal can be stressful for both parties. You have to relocate most of your property on the affected area to a new location and adjust your daily operation. The last thing we want to do is add to that. Hence, we take a proactive, customer-focused approach on all our floor installation. We will assist you with your property relocation and covering and ensure a quick and smooth process.</p>
  </div>
  <div class="divider" style="left:430px"></div>
  <div class="feature" style="left:444px">
    <div class="icon" style="background:linear-gradient(180deg,#d9cfb3 0%,#c8c8c8 100%)" role="img" aria-label="Illustration of a tiled floor with stars"></div>
    <h3>A Floor Worthy Of Your Home</h3>
    <p>The quality and type of your floor are as important as its style and appeal. The wrong combination could see you spending a lot on maintenance and feeling frustrated. That's why here at Keystone Group, don't just go with what is available, but what fits best. We will work with you to identify the kind of floor that matches your lifestyle, theme, preference, and strikes a balance between lower maintenance and durability.</p>
  </div>
  <div class="divider" style="left:765px"></div>
  <div class="feature" style="left:790px">
    <div class="icon" style="background:linear-gradient(180deg,#c8c8c8 0%,#d9cfb3 100%)" role="img" aria-label="Illustration of a team of certified experts"></div>
    <h3>Qualified And Certified Experts</h3>
    <p>After spending a lot to finally get that property of your dream, the last thing you want is some rookie messing it up and getting you back on your plans. Here at Keystone Group, we understand this and strive to avoid its occurrence. Hence, we never assign your projects to unvetted professionals. Our team of experts is made up of only highly experienced and passionate individuals licensed in their specific fields to ensure the best results possible.</p>
  </div>
  <div class="warranty">Backed By <b>1-Year</b> Labor Warranty</div>
</section>

<section class="partner abs">
  <h2>A Reliable Partner To Lean On</h2>
  <p>Keystone Group comes with over 14 years of experience in floor installation. We are specialists when it comes to tile installation, hardwood installation, carpet installation, tile backsplash installation, vinyl installation, laminate floor installation, and floor removal. Over the years, we have come to position ourselves as the professional hands our customers need for all their installation and removal needs. With us, you can be assured of on-time performance, professional services, and prime craftsmanship.</p>
  <div class="btn" style="left:117px;top:369px;width:108px;height:31px">Learn More</div>
  <div class="photo" style="left:609px;top:75px;width:231px;height:157px;background:linear-gradient(135deg,#8a8178,#5f5a55)" role="img" aria-label="Photo of mosaic tile being laid on a wall"></div>
  <div class="photo" style="left:860px;top:75px;width:232px;height:157px;background:linear-gradient(135deg,#c9a27a,#8e6a48)" role="img" aria-label="Photo of hands fitting laminate planks"></div>
  <div class="photo" style="left:609px;top:249px;width:143px;height:164px;background:linear-gradient(135deg,#b4b4b0,#7e7d79)" role="img" aria-label="Photo of a worker smoothing a floor screed"></div>
  <div class="photo" style="left:768px;top:249px;width:324px;height:164px;background:linear-gradient(135deg,#e6dccb,#c8b89f)" role="img" aria-label="Photo of carpet being cut with a utility knife"></div>
</section>

<section class="services abs">
  <h2 class="section-title" style="top:62px">Make Your Floors Scream Quality And Beauty</h2>
  <div class="section-sub" style="top:110px">We believe in making it easier for all to work and grow on an International scale</div>

  <div class="card" style="left:114px;top:178px">
    <div class="img" style="background:linear-gradient(135deg,#d7b98c,#8c7356)" role="img" aria-label="Photo of tiles being set on a floor"></div>
    <h3 class="accent">Tile Installation</h3>
    <p>Tile is one durable flooring material that, when placed well, leaves your floor or property looking luxurious and inviting.</p>
    <div class="btn b1">Learn More</div><div class="btn btn-outline b2">Get A Quote</div>
  </div>
  <div class="card" style="left:448px;top:178px">
    <div class="img" style="background:linear-gradient(135deg,#a8552c,#5e2a14)" role="img" aria-label="Photo of hardwood boards being fitted"></div>
    <h3>Hardwood Installation</h3>
    <p>Are you looking for the best hardwood installers near you? You are at the right place. Keystone Group is an expert in all kinds of hardwood installation.</p>
    <div class="btn b1">Learn More</div><div class="btn btn-outline b2">Get A Quote</div>
  </div>
  <div class="card" style="left:780px;top:178px">
    <div class="img" style="background:linear-gradient(135deg,#c98a4a,#7a4a24)" role="img" aria-label="Photo of a glossy laminate floor in an empty room"></div>
    <h3>Laminate Installation</h3>
    <p>Adorning your floor with laminate material is often a great option to limit scratches, wear and tear, and improve floor durability.</p>
    <div class="btn b1">Learn More</div><div class="btn btn-outline b2">Get A Quote</div>
  </div>

  <div class="card" style="left:114px;top:635px">
    <div class="img" style="background:linear-gradient(135deg,#e8d2ad,#c79f6c)" role="img" aria-label="Photo of carpet being measured with a tape"></div>
    <h3>Carpet Installation</h3>
    <p>Carpet installation is a good way to personalized the theme of your home, improve comfort, warmth, and a luxurious feel.</p>
    <div class="btn b1">Learn More</div><div class="btn btn-outline b2">Get A Quote</div>
  </div>
  <div class="card" style="left:448px;top:635px">
    <div class="img" style="background:linear-gradient(135deg,#eeeeec,#bfc2c4)" role="img" aria-label="Photo of a gloved hand laying vinyl planks"></div>
    <h3>Vinyl Installation</h3>
    <p>Vinyl flooring is a great option for families and businesses looking for a balance between the deep texture and feel of real wood, tiles, &amp; stones</p>
    <div class="btn b1">Learn More</div><div class="btn btn-outline b2">Get A Quote</div>
  </div>
  <div class="card" style="left:780px;top:635px">
    <div class="img" style="background:linear-gradient(135deg,#9b7a5c,#4f3b2b)" role="img" aria-label="Photo of old floor tiles being removed"></div>
    <h3>Floor Removal</h3>
    <p>Removing your floor isn't an easy task, whether it is a carpet installation, hardwood, or concrete. It takes a lot of time and is filled with risks.</p>
    <div class="btn b1">Learn More</div><div class="btn btn-outline b2">Get A Quote</div>
  </div>
</section>

<section class="reviews abs">
  <div class="map" role="img" aria-label="Faint dotted world map background"></div>
  <h2><b>We are</b> very happy to<br>get client's review!</h2>

  <div class="review" style="left:85px">
    <div class="avatar" role="img" aria-label="Client portrait"></div><div class="quote">&#8220;</div>
    <div class="stars">★★★★★</div>
    <p>Lorem ipsum dolor sit amet, consecte sed do eiusmod tempor incididunt utlao bore et dolore magna aliqua.</p>
    <div class="name">Nadia Brooks, <span>Agent Manager</span></div>
  </div>
  <div class="review" style="left:437px">
    <div class="avatar" role="img" aria-label="Client portrait"></div><div class="quote">&#8220;</div>
    <div class="stars">★★★★★</div>
    <p>Lorem ipsum dolor sit amet, consecte sed do eiusmod tempor incididunt utlao bore et dolore magna aliqua.</p>
    <div class="name">Nadia Brooks, <span>Agent Manager</span></div>
  </div>
  <div class="review" style="left:789px">
    <div class="avatar" role="img" aria-label="Client portrait"></div><div class="quote">&#8220;</div>
    <div class="stars">★★★★★</div>
    <p>Lorem ipsum dolor sit amet, consecte sed do eiusmod tempor incididunt utlao bore et dolore magna aliqua.</p>
    <div class="name">Nadia Brooks, <span>Agent Manager</span></div>
  </div>
  <div class="dots"><i></i><i></i></div>
</section>

<section class="process abs">
  <h2 class="section-title">A Simple, Repeatable Process</h2>
  <div class="section-sub">A Process to Complete the Job Successfully</div>

  <div class="step" style="left:56px">
    <div class="circle"><svg width="40" height="40" viewBox="0 0 40 40" fill="none" stroke="#fff" stroke-width="2"><rect x="5" y="8" width="26" height="24"/><line x1="5" y1="15" x2="31" y2="15"/><line x1="11" y1="4" x2="11" y2="10"/><line x1="25" y1="4" x2="25" y2="10"/></svg></div>
    <h4>Schedule An Appointment</h4>
    <p>Fill out the form on our site or call us on our hotline to relay your needs and schedule a free site inspection. It is that simple!</p>
  </div>
  <div class="step" style="left:344px">
    <div class="circle"><div class="fill" role="img" aria-label="Icon of a floor tile"></div></div>
    <h4>Your Preferred Floor Material</h4>
    <p>Based on our findings on consultation and our inspection, we will help you figure out the right type of floor for your home or business space.</p>
  </div>
  <div class="step" style="left:626px">
    <div class="circle"><div class="fill" role="img" aria-label="Icon of an installer at work"></div></div>
    <h4>Premium Installation</h4>
    <p>After the two stages are done, and you have approved the work date, our professionals for your floor will begin work on your property.</p>
  </div>
  <div class="step" style="left:907px">
    <div class="circle"><div class="fill" role="img" aria-label="Icon of a satisfied customer"></div></div>
    <h4>A Happy You!</h4>
    <p>With a quality job done, go ahead and enjoy your floors for years to come with minimal maintenance on your side!</p>
  </div>
</section>

<section class="get-started abs">
  <h2>GET STARTED NOW</h2>
  <p class="lead">Loeiusmod tempor incididun rem ipsum dolor sit amet consectetur adipiscing elitsede.</p>
  <div class="field" style="left:442px;top:133px">Name</div>
  <div class="field" style="left:679px;top:133px">Contact Info</div>
  <div class="field" style="left:908px;top:133px">Address</div>
  <div class="field" style="left:442px;top:220px">Type of Appointment</div>
  <div class="field" style="left:679px;top:220px">Closest City</div>
  <div class="field" style="left:908px;top:220px">Date</div>
  <div class="submit">Submit</div>
</section>

<footer class="footer abs">
  <div class="brand" style="left:108px;top:72px;font-size:19px"><span class="brand-mark" style="width:12px;height:12px"></span>KEYSTONE FLOORING FLORIDA</div>
  <div class="search">Search...<svg style="position:absolute;right:10px;top:9px" width="14" height="14" viewBox="0 0 14 14" fill="none" stroke="#333" stroke-width="2"><circle cx="6" cy="6" r="4.5"/><line x1="9.5" y1="9.5" x2="13" y2="13"/></svg></div>
  <ul class="contact-list">
    <li>(02) 555-018-2240</li>
    <li>hello@keystonefloors.example</li>
    <li>42 Harbor Lane Cedar Point, FL<br><span style="padding-left:20px">32000, USA</span></li>
  </ul>
  <div class="social" style="left:108px;top:258px;gap:12px"><i style="width:20px;height:20px;background:#3b5998"></i><i style="width:20px;height:20px;background:#1da1f2"></i><i style="width:20px;height:20px;background:#e62117"></i></div>
  <div class="col" style="left:371px"><h5>Useful Resources</h5><ul><li>Home</li><li>About Us</li><li>Our Contacts</li><li>Partners</li></ul></div>
  <div class="col" style="left:597px"><h5>Our Company</h5><ul><li>Tech Labs</li><li>Company Story</li><li>Latest News</li><li>Shop</li></ul></div>
  <div class="promise">
    <h5>OUR PROMISE TO YOU</h5>
    <ul><li>Free Worldwide Delivery</li><li>No Hassle Refund Policy</li><li>Monthly payments scheme</li><li>Safe verified methods</li></ul>
  </div>
  <div class="pay"><i style="background:#2a4a9b"></i><i style="background:#1b3f8f"></i><i style="background:#24439a"></i><i style="background:#3c78c8"></i></div>
</footer>

<div class="bottom-bar abs">
  <span class="abs" style="left:108px;top:21px">© 2020 Keystone Flooring Florida</span>
  <span class="abs" style="left:870px;top:21px">Privacy Policy</span>
  <span class="abs" style="left:955px;top:16px;height:22px;border-left:1px solid #ccc"></span>
  <span class="abs" style="left:985px;top:21px">Terms of Service</span>
</div>

</body>
</html>
```